Vice chair

I'm running for a position as vice chair this will be posted in the lunch room cafeteria in this package i posted logos, my picture, sample of old flyers to give you a idea i also wrote literature need help in putting it together like it to look like a million bucks goal win this election I summited lots of pdf files and jpeg look though them to help with your design feel free to contact me to further assist you
Updates

Would like this to be completed by Wednesday

Target Market(s)

My constituents

Font styles to use
Serif

Colors

Designer to choose colors to be used in the design.

Requirements
Must have
• Make it look clean neat
Nice to have
• Nice background

```html
<!DOCTYPE html>
<html lang="en">
<head>
<meta charset="utf-8">
<title>Vice Chair Campaign Poster</title>
<link href="https://fonts.googleapis.com/css2?family=Archivo+Black&family=Roboto:wght@400;500;700;900&display=swap" rel="stylesheet">
<style>
  :root {
    --page-bg: #ecebea;
    --paper: #ffffff;
    --ink: #141414;
    --flag-red: #e8202f;
    --flag-blue: #2d2f8f;
    --accent-red: #e3101f;
  }
  html, body {
    margin: 0;
    width: 1200px;
    height: 1200px;
    overflow: hidden;
    background: var(--page-bg);
  }
  .poster {
    position: absolute;
    left: 206px;
    top: 20px;
    width: 788px;
    height: 1160px;
    background: var(--paper);
    overflow: hidden;
    font-family: "Roboto", Arial, sans-serif;
    color: var(--ink);
  }
  .backdrop { position: absolute; left: 0; top: 0; }
  .portrait {
    position: absolute;
    left: 38px;
    top: 36px;
    width: 368px;
    height: 368px;
    border-radius: 50%;
    border: 7px solid var(--paper);
    box-sizing: border-box;
    background: radial-gradient(circle at 45% 45%, #a8795c 0%, #7a5240 45%, #3e5a5a 85%, #2b6b7a 100%);
  }
  .headline {
    position: absolute;
    right: 24px;
    top: 70px;
    margin: 0;
    text-align: right;
    white-space: nowrap;
    font-family: "Archivo Black", "Roboto", sans-serif;
    font-style: italic;
    font-weight: 400;
    line-height: 0.88;
    letter-spacing: -2px;
    color: var(--ink);
  }
  .headline .big { font-size: 58px; }
  .headline .small { font-size: 38px; }
  .headline .line2 { display: block; font-size: 64px; letter-spacing: -3px; }
  .depot-badges {
    position: absolute;
    left: 441px;
    top: 236px;
    display: flex;
    gap: 18px;
  }
  .depot-badge {
    width: 94px;
    height: 94px;
    border-radius: 50%;
    box-sizing: border-box;
  }
  .depot-badge.gold { background: #f4d41a; border: 5px solid var(--flag-red); }
  .depot-badge.blue { background: #2f5fc4; border: 5px solid #ffffff; box-shadow: 0 0 0 2px var(--flag-blue); }
  .depot-badge.orange { background: #f08a1c; border: 5px solid var(--flag-red); }
  .statement {
    position: absolute;
    left: 38px;
    top: 484px;
    width: 702px;
    font-size: 19.8px;
    line-height: 24.4px;
    text-align: justify;
  }
  .statement p { margin: 0 0 5px; }
  .highlights {
    position: absolute;
    left: 48px;
    top: 726px;
    width: 670px;
    margin: 0;
    padding: 0;
    list-style: none;
    color: var(--accent-red);
    font-size: 15.8px;
    line-height: 19.6px;
  }
  .highlights li {
    position: relative;
    padding-left: 25px;
    margin-bottom: 6px;
  }
  .highlights li::before {
    content: "\2605";
    position: absolute;
    left: 0;
    top: 0;
    font-size: 15px;
  }
  .call-to-action {
    position: absolute;
    left: 0;
    top: 932px;
    width: 788px;
    text-align: center;
    margin: 0;
    color: var(--accent-red);
    font-size: 21px;
    font-weight: 500;
  }
  .slogan { position: absolute; left: 0; top: 932px; }
  .slogan text {
    font-family: "Roboto", sans-serif;
    font-weight: 900;
    font-size: 62px;
    fill: var(--flag-blue);
  }
  .ballot-box { position: absolute; left: 350px; top: 1022px; }
</style>
</head>
<body>
  <main class="poster">
    <svg class="backdrop" width="788" height="1160" viewBox="0 0 788 1160" aria-hidden="true">
      <defs>
        <linearGradient id="blueWash" x1="0" y1="0" x2="0" y2="1">
          <stop offset="0" stop-color="#3d3fa3"/>
          <stop offset="0.7" stop-color="#6d73c6"/>
          <stop offset="1" stop-color="#c9cbee"/>
        </linearGradient>
        <linearGradient id="redWash" x1="0" y1="0" x2="1" y2="1">
          <stop offset="0" stop-color="#e9232f"/>
          <stop offset="0.7" stop-color="#f25e66"/>
          <stop offset="1" stop-color="#fbd0d3"/>
        </linearGradient>
      </defs>
      <path fill="url(#blueWash)" d="M0 0 H240 C300 60 360 160 400 260 C430 330 520 340 560 380 C600 420 590 470 520 500 C440 540 330 560 260 560 C170 560 80 520 0 400 Z"/>
      <path fill="url(#redWash)" d="M230 0 H788 V240 C760 260 720 250 690 280 C650 320 640 360 600 380 C540 400 470 370 420 330 C380 290 360 220 320 160 C290 110 250 60 230 0 Z"/>
      <path fill="#7f84cf" opacity="0.7" d="M520 320 C570 330 620 380 600 430 C580 470 520 480 480 460 C450 430 470 340 520 320 Z"/>
      <g fill="#ffffff">
        <polygon points="128,420 134,436 151,436 137,446 142,462 128,452 114,462 119,446 105,436 122,436"/>
        <polygon points="255,440 262,460 283,460 266,472 272,492 255,480 238,492 244,472 227,460 248,460"/>
        <polygon points="408,340 416,362 440,362 421,376 428,398 408,385 388,398 395,376 376,362 400,362"/>
        <polygon points="370,480 375,494 390,494 378,503 382,517 370,508 358,517 362,503 350,494 365,494"/>
        <polygon points="478,405 483,418 497,418 486,426 490,440 478,432 466,440 470,426 459,418 473,418"/>
      </g>
      <polygon fill="#f04a55" points="420,30 424,42 437,42 427,50 431,62 420,55 409,62 413,50 403,42 416,42"/>
    </svg>

    <div class="portrait" role="img" aria-label="Portrait photo of the candidate, Ray Delgado"></div>

    <h1 class="headline"><span class="big">TIME</span> <span class="small">FOR</span><span class="line2">CHANGE</span></h1>

    <div class="depot-badges">
      <div class="depot-badge gold" role="img" aria-label="Depot badge"></div>
      <div class="depot-badge blue" role="img" aria-label="Depot badge"></div>
      <div class="depot-badge orange" role="img" aria-label="Depot badge"></div>
    </div>

    <section class="statement">
      <p>I Ray Delgado for those who don't know me&nbsp; would like to introduce myself I have always been approachable and helpful whether you are a probationary officer or a veteran operator with knowledge or information. We must protect our union rules for ourselves our future and most important our children.</p>
      <p>I would like this opportunity to run as your vice chair a person you can trust and believe in me positive and motivations are my main keys for progress and for change in my campaugn when there are no leaders to look up to one there­fore must become one I do belive I'm the reight person for this position so please come out and support me and vote me as your vice chair.</p>
    </section>

    <ul class="highlights">
      <li>20 years on the Job</li>
      <li>Past Union member of Carriers Guild local 295 belives in there is a collective bargaining agreement in place and no management is above the law to violate it.</li>
      <li>Past Union member of Carriers Guild local 851 belives a house that is divided cannot stand alone.</li>
      <li>In closing I believe that our union does not stand out individually achievement we must stand for collective advancement for all. We must always continue to stand together, stay together and fight together so we can win together because success is never owned, it is rented and the rent is due every day.</li>
    </ul>

    <p class="call-to-action">VOTE INDEPENDENT ME AS YOUR VICE CHAIR</p>

    <svg class="slogan" width="788" height="110" viewBox="0 0 788 110" aria-label="Vote the State">
      <path id="sloganArc" d="M140 110 Q394 40 648 110" fill="none"/>
      <text text-anchor="middle"><textPath href="#sloganArc" startOffset="50%">VOTE THE STATE</textPath></text>
    </svg>

    <svg class="ballot-box" width="90" height="100" viewBox="0 0 90 100" aria-label="Ballot box">
      <rect x="34" y="6" width="20" height="30" rx="2" fill="#e8f6f2" stroke="#9bbdb5" transform="rotate(12 44 21)"/>
      <path d="M40 20 l4 4 l8 -9" stroke="#4caf50" stroke-width="2.5" fill="none"/>
      <rect x="10" y="38" width="70" height="12" fill="var(--flag-red)"/>
      <rect x="13" y="50" width="64" height="42" fill="var(--flag-blue)"/>
      <rect x="30" y="40" width="30" height="3" fill="#8a0f18"/>
    </svg>
  </main>
</body>
</html>
```